Instructions for nurses on how to give a report on each shift

I have a 2-page reference sheet that needs to be updated to look more aesthetically pleasing.

Target Market(s)

Healthcare, nurses

Industry/Entity Type

Healthcare

Font styles to use
Sans Serif

Requirements
Must have
• Please make sure it is easy to read, the content is well organized and has a flow to it. Please also pick colors that would coordinate with our website www.brivolen.org (so mainly navy and white or off-white with accent colors.) Please make sure to add accent colors to break up the content. The MORVY name and title at the top should remain on the page but I'm not married to the star or logo style. You can do what you think looks best there. Way at the bottom in fine print, I would like for you to add BRIVOLEN © 2019 All rights reserved.

```html
<!DOCTYPE html>
<html lang="en">
<head>
<meta charset="utf-8">
<title>MORVY – Shift Report Reference Sheet</title>
<link rel="stylesheet" href="https://fonts.googleapis.com/css2?family=Poppins:wght@400;500;600&family=Roboto+Condensed:wght@400;700&display=swap">
<style>
:root{
  --navy:#0f3a74;
  --navy-deep:#0a2c5c;
  --blue:#1a64ad;
  --blue-bright:#2a86c8;
  --row:#1c5c9f;
  --paper:#f7f5ea;
  --ink:#1d3557;
  --tick:#5a87b8;
  --grey:#8a8a8a;
  --stage:#e2e2e2;
}
*{box-sizing:border-box;margin:0;padding:0}
html,body{width:1200px;height:854px;overflow:hidden}
body{background:var(--stage);font-family:"Poppins",sans-serif;color:var(--ink);position:relative}
.sheet{position:absolute;top:45px;width:540px;height:764px;background:var(--paper);overflow:hidden}
.sheet--front{left:40px}
.sheet--back{left:620px}
.svg-layer{position:absolute;left:0;top:0}

/* header */
.header-title{position:absolute;left:12px;top:19px;font-family:"Roboto Condensed",sans-serif;line-height:1;white-space:nowrap}
.header-title .kicker{font-size:14px;letter-spacing:.2px;display:block}
.header-title .main{font-size:24px;font-weight:700;letter-spacing:.3px;display:block;margin-top:1px}
.sheet--front .header-title{color:#fff}
.sheet--back .header-title{color:var(--navy)}
.sheet--back .header-title .kicker{color:var(--blue)}
.brand{position:absolute;top:24px;left:400px;display:flex;align-items:center;gap:7px;font-family:"Poppins",sans-serif;font-weight:600;font-size:24px;letter-spacing:1px}
.sheet--front .brand{color:var(--navy)}
.sheet--back .brand{color:#fff}
.brand .dot{width:12px;height:12px;border-radius:50%;background:currentColor}

/* tick lists */
.tick{position:relative;padding-left:13px}
.tick::before{content:"";position:absolute;left:0;top:50%;width:7px;height:7px;margin-top:-4.5px;border:1px solid var(--tick);border-radius:50%}
.tick::after{content:"";position:absolute;left:2.4px;top:50%;width:2.5px;height:1.4px;margin-top:-2.6px;border-left:1px solid var(--tick);border-bottom:1px solid var(--tick);transform:rotate(-45deg)}

/* front: leader block */
.leader-tab{position:absolute;left:0;top:94px;height:26px;width:150px}
.leader-tab span{position:absolute;left:12px;top:3px;font-family:"Roboto Condensed",sans-serif;font-size:19px;color:#fff;letter-spacing:.5px}
.field-label{position:absolute;top:104px;font-size:7.5px;color:var(--ink)}
.prompt{position:absolute;left:30px;height:14px;border-radius:7px;background:var(--blue-bright);color:#fff;font-size:7.5px;line-height:14px;padding:0 7px;white-space:nowrap}
.options{position:absolute;left:250px;width:290px;display:flex;flex-wrap:wrap;column-gap:14px;row-gap:8px;font-size:7.5px;color:var(--ink)}

/* front: checklist table */
.col-head{position:absolute;top:420px;width:90px;margin-left:-45px;text-align:center;color:#fff;font-size:8px;line-height:1.3}
.row-label{position:absolute;left:12px;color:#fff;font-size:11px}
.cell{position:absolute;width:92px;margin-left:-46px;text-align:center;color:#e6eef8;font-size:6px;line-height:1.35}
.num{position:absolute;width:10px;height:10px;margin-left:-5px;border:0.8px solid #c9d8ec;border-radius:50%;color:#c9d8ec;font-size:5.5px;line-height:9px;text-align:center}

/* back: banner */
.banner-main{position:absolute;left:0;width:540px;top:104px;text-align:center;font-family:"Roboto Condensed",sans-serif;font-size:30px;color:#fff;letter-spacing:.3px}
.banner-sub{position:absolute;left:0;width:540px;top:147px;text-align:center;font-family:"Poppins",sans-serif;font-weight:500;font-size:20.5px;color:#fff}

/* back: sections */
.section-tab{position:absolute;height:16px;border-radius:0 8px 8px 0;background:var(--blue-bright);color:#fff;font-size:10px;line-height:16px;padding:0 11px 0 13px;letter-spacing:.3px}
.section-tab--right{border-radius:8px}
.list{position:absolute;list-style:none;font-size:8.6px;line-height:1.3;color:var(--ink)}
.list li{margin-bottom:5.6px}
.list li.tick::before,.list li.tick::after{top:6px}
.divider{position:absolute;left:281px;top:262px;width:1px;height:272px;background:#d8d5c6}

/* footer */
.address{position:absolute;left:30px;top:733px;color:#fff;font-family:"Roboto Condensed",sans-serif;font-size:10.5px;display:flex;align-items:center;gap:5px}
.contacts{position:absolute;left:280px;top:733px;display:flex;gap:10px;font-family:"Roboto Condensed",sans-serif;font-size:10px;color:var(--navy)}
.contacts span{display:flex;align-items:center;gap:3px}
.icon{width:9px;height:9px;border-radius:50%;background:var(--navy);display:inline-block}
.icon--light{background:#fff}
.fine-print{position:absolute;left:0;width:540px;top:706px;text-align:center;font-size:6.5px;color:var(--grey);letter-spacing:.2px}
</style>
</head>
<body>

<!-- FRONT SHEET -->
<section class="sheet sheet--front">
  <svg class="svg-layer" width="540" height="764" viewBox="0 0 540 764" aria-hidden="true">
    <defs>
      <linearGradient id="bandFront" x1="0" y1="0" x2="1" y2="0">
        <stop offset="0" stop-color="#0a2c5c"/><stop offset="1" stop-color="#1a64ad"/>
      </linearGradient>
      <linearGradient id="lowerFront" x1="0" y1="0" x2="0" y2="1">
        <stop offset="0" stop-color="#0a2c5c"/><stop offset="1" stop-color="#174f92"/>
      </linearGradient>
    </defs>
    <polygon points="0,0 382,0 328,70 0,70" fill="url(#bandFront)"/>
    <polygon points="350,0 540,0 540,8 343,8" fill="#1a64ad"/>
    <polygon points="372,0 386,0 336,64 322,64" fill="#2a86c8"/>
    <polyline points="404,8 336,84 378,84" fill="none" stroke="#2a86c8" stroke-width="0.8"/>
    <circle cx="378" cy="84" r="1.6" fill="#2a86c8"/>
    <polygon points="0,94 125,94 107,120 0,120" fill="#1a64ad"/>
    <line x1="128" y1="94" x2="111" y2="120" stroke="#1a64ad" stroke-width="1.2"/>
    <line x1="14" y1="120" x2="14" y2="333" stroke="#2a86c8" stroke-width="0.8"/>
    <g stroke="#2a86c8" stroke-width="0.8">
      <line x1="14" y1="151" x2="30" y2="151"/><line x1="14" y1="191" x2="30" y2="191"/>
      <line x1="14" y1="253" x2="30" y2="253"/><line x1="14" y1="293" x2="30" y2="293"/>
      <line x1="14" y1="333" x2="30" y2="333"/>
    </g>
    <polygon points="0,352 270,404 540,346 540,699 0,699" fill="url(#lowerFront)"/>
    <circle cx="270" cy="398" r="9" fill="#f7f5ea" stroke="#1a64ad" stroke-width="1.2"/>
    <polyline points="265,396 270,401 275,396" fill="none" stroke="#1a64ad" stroke-width="1.4"/>
    <rect x="53" y="477" width="487" height="53" fill="#1c5c9f"/>
    <rect x="53" y="542" width="487" height="157" fill="#1c5c9f"/>
    <polygon points="0,722 296,722 278,754 0,754" fill="#0f3a74"/>
    <polygon points="0,738 20,764 0,764" fill="#8a8a8a"/>
    <line x1="300" y1="738" x2="312" y2="754" stroke="#0f3a74" stroke-width="0.8"/>
    <rect x="0" y="757" width="540" height="2" fill="#2a86c8"/>
    <rect x="0" y="759" width="540" height="5" fill="#0f3a74"/>
    <rect x="120" y="752" width="420" height="1" fill="#2a86c8"/>
  </svg>

  <div class="header-title">
    <span class="kicker">LEADING EFFECTIVELY BY ADVOCATING AND</span>
    <span class="main">DELIVERING EXCELLENCE</span>
  </div>
  <div class="brand"><span class="dot"></span>MORVY</div>

  <div class="leader-tab"><span>LEADER</span></div>
  <div class="field-label" style="left:122px">Name :</div>
  <div class="field-label" style="left:244px">Title :</div>
  <div class="field-label" style="left:372px">Assignment :</div>

  <div class="prompt" style="top:144px">Any change in resident status?</div>
  <div class="options" style="top:147px">
    <span class="tick">Admissions</span><span class="tick">Discharges</span><span class="tick">Transfers</span><span class="tick">Appointments</span>
  </div>

  <div class="prompt" style="top:184px">Any concerning changes in resident's condition?</div>
  <div class="options" style="top:187px">
    <span class="tick">Pain</span><span class="tick">Ambulation</span><span class="tick">Behavior</span><span class="tick">Appetite</span><span class="tick">Skin</span>
    <span class="tick">Elimination</span><span class="tick">Safety</span>
  </div>

  <div class="prompt" style="top:246px">Any residents requiring extraordinary monitoring?</div>
  <div class="options" style="top:249px">
    <span class="tick">Falls</span><span class="tick">Decline in condition</span><span class="tick">IV/ABT therapy</span><span class="tick">Hospice</span>
  </div>

  <div class="prompt" style="top:286px">Any concerns related to residents environment?</div>
  <div class="options" style="top:289px">
    <span class="tick">Room temperature</span><span class="tick">Supplies</span><span class="tick">Equipment</span>
  </div>

  <div class="prompt" style="top:326px">Any concerns related to residents environment?</div>
  <div class="options" style="top:329px">
    <span class="tick">Supplies</span><span class="tick">Acuity</span><span class="tick">Time constraints</span><span class="tick">Family requests</span>
    <span class="tick">Environment</span>
  </div>

  <div class="col-head" style="left:98px">Any change<br>in resident<br>status?</div>
  <div class="col-head" style="left:192px">Any concerning<br>changes in<br>resident's<br>condition?</div>
  <div class="col-head" style="left:294px">Any residents<br>requiring<br>extraordinary<br>monitoring?</div>
  <div class="col-head" style="left:390px">Any concerns<br>related to<br>residents<br>environment?</div>
  <div class="col-head" style="left:484px">Any concerns<br>related to<br>residents<br>environment?</div>

  <div class="row-label" style="top:496px">NO</div>
  <div class="row-label" style="top:561px">YES</div>

  <div class="cell" style="left:98px;top:486px">I do not have any<br>actual or expected<br>changes in<br>resident status.</div>
  <div class="cell" style="left:192px;top:486px">I have no residents<br>with concerning<br>changes in their<br>condition.</div>
  <div class="cell" style="left:294px;top:486px">I have no residents<br>requiring<br>extraordinary<br>monitoring.</div>
  <div class="cell" style="left:390px;top:486px">I have no concerns<br>related to my<br>residents<br>environment</div>
  <div class="cell" style="left:484px;top:486px">I have no concerns<br>or barriers affecting<br>my ability to perform<br>my job</div>

  <div class="cell" style="left:98px;top:552px">My residents<br>with changes in<br>their status are</div>
  <div class="cell" style="left:192px;top:552px">My residents<br>w/ concerning changes<br>in their condition include</div>
  <div class="cell" style="left:294px;top:552px">My residents that<br>require extraordinary<br>monitoring are</div>
  <div class="cell" style="left:390px;top:552px">My residents with<br>concerns related to<br>their environment include</div>
  <div class="cell" style="left:484px;top:552px">My concerns affecting<br>my ability to perform<br>my job include</div>

  <div class="num" style="left:98px;top:590px">1</div><div class="num" style="left:192px;top:590px">1</div><div class="num" style="left:294px;top:590px">1</div><div class="num" style="left:390px;top:590px">1</div><div class="num" style="left:484px;top:590px">1</div>
  <div class="num" style="left:98px;top:627px">2</div><div class="num" style="left:192px;top:627px">2</div><div class="num" style="left:294px;top:627px">2</div><div class="num" style="left:390px;top:627px">2</div><div class="num" style="left:484px;top:627px">2</div>
  <div class="num" style="left:98px;top:663px">3</div><div class="num" style="left:192px;top:663px">3</div><div class="num" style="left:294px;top:663px">3</div><div class="num" style="left:390px;top:663px">3</div><div class="num" style="left:484px;top:663px">3</div>

  <div class="fine-print">BRIVOLEN © 2019 All rights reserved.</div>

  <div class="address"><span class="icon icon--light"></span>18 North Alder Ave., Suite 210B, Fairhaven, IL 60219</div>
  <div class="contacts">
    <span><i class="icon"></i>630-555-0142</span>
    <span><i class="icon"></i>info@brivolen.org</span>
    <span><i class="icon"></i>www.brivolen.org</span>
  </div>
</section>

<!-- BACK SHEET -->
<section class="sheet sheet--back">
  <svg class="svg-layer" width="540" height="764" viewBox="0 0 540 764" aria-hidden="true">
    <defs>
      <linearGradient id="bannerBack" x1="0" y1="0" x2="0" y2="1">
        <stop offset="0" stop-color="#0a2c5c"/><stop offset="1" stop-color="#1a64ad"/>
      </linearGradient>
      <linearGradient id="barBack" x1="0" y1="0" x2="1" y2="0">
        <stop offset="0" stop-color="#1a64ad"/><stop offset=".5" stop-color="#2a86c8"/><stop offset="1" stop-color="#1a64ad"/>
      </linearGradient>
    </defs>
    <polygon points="250,0 540,0 540,8 244,8" fill="#0f3a74"/>
    <polygon points="346,8 540,8 540,70 300,70" fill="#1a64ad"/>
    <polygon points="336,8 346,8 300,70 290,70" fill="#2a86c8"/>
    <polyline points="378,12 336,75 378,75" fill="none" stroke="#0f3a74" stroke-width="0.8"/>
    <circle cx="378" cy="75" r="1.6" fill="#0f3a74"/>
    <polygon points="0,70 540,70 540,186 270,230 0,186" fill="url(#bannerBack)"/>
    <polygon points="34,104 506,104 490,146 50,146" fill="url(#barBack)"/>
    <polygon points="14,104 30,104 46,146 30,146" fill="#2a86c8"/>
    <polygon points="510,104 526,104 510,146 494,146" fill="#2a86c8"/>
    <circle cx="270" cy="227" r="9" fill="#f7f5ea" stroke="#1a64ad" stroke-width="1.2"/>
    <polyline points="265,225 270,230 275,225" fill="none" stroke="#1a64ad" stroke-width="1.4"/>
    <polygon points="0,722 296,722 278,754 0,754" fill="#0f3a74"/>
    <polygon points="0,738 20,764 0,764" fill="#8a8a8a"/>
    <line x1="300" y1="738" x2="312" y2="754" stroke="#0f3a74" stroke-width="0.8"/>
    <rect x="0" y="757" width="540" height="2" fill="#2a86c8"/>
    <rect x="0" y="759" width="540" height="5" fill="#0f3a74"/>
    <rect x="120" y="752" width="420" height="1" fill="#2a86c8"/>
  </svg>

  <div class="header-title">
    <span class="kicker">LEADING EFFECTIVELY BY ADVOCATING AND</span>
    <span class="main">DELIVERING EXCELLENCE</span>
  </div>
  <div class="brand"><span class="dot"></span>MORVY</div>

  <div class="banner-main">WHEN “I” IS REPLACED BY “WE”</div>
  <div class="banner-sub">EVEN ILLNESS BECOMES WELLNESS</div>

  <div class="divider"></div>

  <div class="section-tab" style="left:0;top:237px">OBJECTIVES</div>
  <ul class="list" style="left:14px;top:259px;width:262px">
    <li class="tick">Accountability : Declare roles and assignments</li>
    <li class="tick">Advocacy : Identify patient needs</li>
    <li class="tick">Critical Thinking : Prioritize and recognize obstacles</li>
    <li class="tick">Communication : Share important information</li>
    <li class="tick">Collaboration : Utilize an interdisciplinary approach</li>
  </ul>

  <div class="section-tab section-tab--right" style="left:303px;top:237px">OUTCOMES</div>
  <ul class="list" style="left:318px;top:259px;width:222px">
    <li class="tick">Share best practices</li>
    <li class="tick">Improve communication</li>
    <li class="tick">Promote cohesiveness</li>
    <li class="tick">Increase staff morale</li>
    <li class="tick">Enhance patient and organizational outcomes</li>
  </ul>

  <div class="section-tab" style="left:0;top:371px">WHO</div>
  <ul class="list" style="left:14px;top:394px;width:262px">
    <li class="tick">All nurses on the unit</li>
    <li class="tick">All nursing support staff (CNA/MA/HCT)</li>
    <li class="tick">Administrator</li>
    <li class="tick">Director of Nursing</li>
    <li class="tick">Head of pertinent disciplines (Dietary, Social Work, Physical Therapy, Engineering, Central Supply, etc.)</li>
  </ul>

  <div class="section-tab section-tab--right" style="left:303px;top:371px">WHEN</div>
  <ul class="list" style="left:318px;top:394px;width:210px">
    <li class="tick">Every morning ( assign&nbsp; a meeting time for each unit ).</li>
    <li class="tick">Keep meetings within 15 minutes in length.</li>
  </ul>

  <div class="section-tab section-tab--right" style="left:303px;top:458px">WHERE</div>
  <ul class="list" style="left:318px;top:481px;width:210px">
    <li class="tick">Nursing station on each unit</li>
  </ul>

  <div class="section-tab" style="left:0;top:514px">HELPFUL TIPS</div>
  <ul class="list" style="left:14px;top:536px;width:520px">
    <li class="tick">Assign a meeting facilitator (usually the administrator of the facility)</li>
    <li class="tick">Standing during meetings keeps the meetings short and to the point</li>
    <li class="tick">Keeping meetings within 15 minutes emphasizes being prepared and direct</li>
    <li class="tick">Keep meeting times consistent (morning is best)</li>
    <li class="tick">Do not begin until everyone is present (minimizes stragglers)</li>
    <li class="tick">Avoid discussing personal concerns</li>
    <li class="tick">Include reminders for in-services, meetings, etc. and updates towards the end of the meeting</li>
    <li class="tick">Always conclude with achievements, milestones, praise, words of encouragement, motivational quote, etc.</li>
  </ul>

  <div class="fine-print">BRIVOLEN © 2019 All rights reserved.</div>

  <div class="address"><span class="icon icon--light"></span>18 North Alder Ave., Suite 210B, Fairhaven, IL 60219</div>
  <div class="contacts">
    <span><i class="icon"></i>630-555-0142</span>
    <span><i class="icon"></i>info@brivolen.org</span>
    <span><i class="icon"></i>www.brivolen.org</span>
  </div>
</section>

</body>
</html>
```